Guarenteed! - Homepage Website Design - Coding not required- Winner to complete further pages

Hi all,

We're looking at redesigning our current website with a few adjustments to other pages but the main adjustments will be on the homepage which is what this design request is for. Please note : any of these ideas can be changed if you have something particularly different / special in mind etc.

P.S Coding is not required, just a design.

- Our website -

Our website is simply a price comparison website that allows customers to find companies within their area at the best price. The products available are mostly related to the vehicle trade and all refer to vinyl. This includes the likes of vehicle window tint, vehicle colour change vehicle wrap, vehicle signage as well as other cosmetic vinyl modifications. We allow the customer to search for their product within their chosen area and receive a list of companies who supply their product within that area. From here they can compare prices and view further details on the company.

- What we're looking to do -

We're looking first of all to adjust how the website homepage is displayed, this includes adding images and adjusting the colours that are explained below:

First of all, we look to spread out each of the 12 products (which can be seen on the website as it stands) and add an image to each of the products (all being spaced out as shown in our sketch)

We've been told the website looks too busy so we're thinking if we adjust the colours to more simplier neutral colours as well as the main focus of the website being on the 12 images, that would be great.

- Logo + Banner -

Logo to remain top left although banner may be removed / adjusted to make simplier.

- Colours -

Adjustments - Colours shades
We want the website to still look exciting but simplify the colours. Needs to be kept up to date with the colours / textures etc (bright colours to highlight keypoints)
We're still looking to use either blue or orange or maybe both to highlight these keypoints but the main website to be light colours and maybe even black on white background. The entire homepage can be adjusted colour wise if you feel it fits into your theme including menu bars, banners etc. The key is to get this right with being not too overpowering with the colours but still look interesting and up to date.

- 1 - 4 steps banner - (text may change)

This sits just under the logo and explains to the user how easy the website is to use and the steps they need to take. This may change to a 1 - 5 steps but we're looking to have this designed once the overall colours / theme of the website is sorted.

- 12 images - 4 x 3

This is the main focus of the website and will be the main focus of what the customer sees first of all. This will be where they select their product and then underneath, enter their postcode and distance they would like to search within. As explained further up, we have some of the product images available so if you can where possible add these to the design and then duplicate the images on those we currently don't have available.

- 12 Images -Titles -

These titles will be in this order from left to right and etc

- Colour Change Wrap
- Printed Vehicle Wrap
- Window Tint
- Headlight Tint
- Vehicle Signage
- Shop Signage
- Roof Vinyl Wrap
- Bonnet Vinyl Wrap
- Carbon Fibre Vinyl
- Stickerbomb Vinyl
- Clear Protective Vinyl
- Wheel Refurb

Text to be quite large, centered and with the o to the left of the title. Short titles like 'Window Tint' should fit on one line in the middle of the box where as titles such as ' Stickerbomb Vinyl Wrap' should have the 'Stickerbomb Vinyl' on the first line with the 'Wrap' on the line below. The background of this text is up to experient, might be worth just a simple colour or it might be worth using a bright blue or orange to keep in with the theme of the logo etc.

These will also have the circle tick box to the left of the title (as on the current website) where the customer clicks to select the product they have available.
We were also thinking that if when the customer ticks the circle on their selected box, the box is highlighted in some way to show this.

- Search Block -

This will appear under the 12 images and allows the customer to input their postcode and distance for the search criteria. Colours on this can of course be adjusted to keep in theme with the website.

- Under the 12 Images -

- Block underneath the 12 images and search block -

To the left will be some key bullet points about the website - maybe 4 or 5 with a green tick to the left of this. Background colour will probably be best to be a light colour, possibly grey.

Then to the right of this will appear 4 images, 2 before and 2 after when applying these products. Images to be used aren't fully decided on and we would like this stage of the design left to the end when the rest of the theme etc have been decided on.

Attached images are as follows :
- How the website looks as it stands
- The fold line on the website (obviously important)
- Our rough sketch of how we'd like the website homepage to look.
- We have 7 of the images ready that are all attached in this one file. Please duplicate the images on those that currently don't have the image available.

We will also be requesting a website developer to put this into action if our current designer falls through so please feel free to contact us if potentially interested.

The layout can change if you can think of something particular different / unique that works with this design. The main idea is to not only get the 12 products on view to the viewers but also the keypoints and before and after images.

Any questions, please ask away as we're bound to have forgotten a few things.

Thanks and good luck!

Hi all, keep the designs coming.

We haven't quite seen that extra special design we're after. As stated, we're after something fairly simple to suit the youth as well as the middle aged but we're also after something that bit special.

Colours to concentrate on are still and orange etc although feel free to use other colours if you have anything special in mind.

Please experience and we'll give you our honest feedback.

Many thanks all and good luck!

Hi all, this is a message to all the designers.

Some good designs coming in but we're still after that something special for the website design. Keep the designs coming and please feel free to experiment with the design colours, layout etc.

The basic principle of the website needs to remain regarding the 12 products, search within block and 4 steps all appearing on the homepage.

The 4 steps seems to work best when it's got text as well as some simple images next to this.

A variation with the product titles with how to display this, some designers have gone with a simple white background whereas others have gone with colours. Please experiment here and where possible, add a contract / texture to the colour. Please remember the product titles needs to be clear, centured and with the circle tick box to the left of it. 

We're after a fairly simple design although we need it to look 21st century, up to date as well as interesting. The key points straight away are the 4 steps as well as the 12 products so try to guide the viewer to these areas a little.

White background behind the 12 images seems to be a much, although a light colour could possibly work.

The keypoints underneath these 12 products are too very important as it outlines what we do etc. Tick colour can vary.

Next to these keypoints will be the 'before' and 'after' images, these images needs to be fairly small and ensure there is white background around the image itself.

Good luck all and any questions, feel free to ask away.

Thanks!

Hi,

 Thank you for your time and effort with these designs, we are very nearly there with the design but we've thought of something that may work for the homepage. A curved arrow from step 1 pointing to the products, this may or may not work but feel free to give it a go.

Many thanks,

Thank you to everyone for your time and efforts with the design. It's hugely appreciated so thank you all once again.

Wish you all the luck in the future.

```html
<!DOCTYPE html>
<html lang="en">
<head>
<meta charset="utf-8">
<title>Wrapfinder – Find and Compare Vinyl Installers</title>
<link href="https://fonts.googleapis.com/css2?family=Oswald:wght@400;500;600&family=Play:wght@400;700&display=swap" rel="stylesheet">
<style>
:root{
  --orange:#f39a2e;
  --orange-light:#fbb255;
  --blue-deep:#0b2a7a;
  --blue-text:#2c4a9a;
  --panel:#dfe3ee;
  --band:#dbe3f3;
  --grey-dark:#3d3d3d;
  --grey-darker:#2f2f2f;
  --white:#ffffff;
  --text-dark:#4a4a4a;
  --tick:#5fc33b;
  --tile-edge:#dde0e6;
}
*{box-sizing:border-box;margin:0;padding:0}
html,body{width:1200px;height:2209px;overflow:hidden}
body{position:relative;background:var(--white);font-family:"Play",sans-serif}
.abs{position:absolute}

/* header */
.site-header{left:0;top:0;width:1200px;height:97px;background:var(--white)}
.brand{left:147px;top:31px;display:flex;align-items:center;gap:12px}
.brand-dot{width:34px;height:34px;border-radius:50%;background:var(--orange)}
.brand-name{font-family:"Oswald",sans-serif;font-weight:600;font-size:34px;letter-spacing:1px;color:var(--blue-deep)}
.main-nav{right:145px;top:34px;display:flex;height:49px;align-items:center;font-family:"Oswald",sans-serif;font-size:13px;color:var(--text-dark)}
.main-nav a{color:inherit;text-decoration:none;padding:0 16px;border-left:1px solid #ddd;line-height:14px}
.main-nav a:first-child{border:0}
.main-nav a.active{background:var(--orange);color:var(--white);line-height:49px;padding:0 14px}

/* backdrop */
.backdrop{left:0;top:97px;width:1200px;height:1692px;
  background:
    linear-gradient(170deg,rgba(255,255,255,0) 55%,rgba(90,150,255,.25) 62%,rgba(255,255,255,0) 70%),
    radial-gradient(ellipse at 50% 30%,#2f63d4 0%,#1a48b5 35%,#0c2f86 70%,#07215f 100%)}

/* tagline band */
.tagline{left:144px;top:97px;width:911px;height:128px;background:var(--band);text-align:center}
.tagline::before,.tagline::after{content:"";position:absolute;left:0;right:0;height:1px;background:rgba(255,255,255,.9)}
.tagline::before{top:16px}.tagline::after{bottom:16px}
.tagline-lead{margin-top:42px;font-size:18px;letter-spacing:.5px;color:#555}
.tagline-strong{margin-top:2px;font-size:24px;font-weight:700;letter-spacing:2px;color:var(--blue-text)}

/* slider */
.hero-slide{left:144px;top:252px;width:911px;height:350px;
  background:
    radial-gradient(ellipse 32% 42% at 56% 52%,#f2f2f0 0%,#cfcfcc 45%,rgba(120,118,112,0) 100%),
    linear-gradient(180deg,#8f8a80 0%,#5f5a52 35%,#2c2925 70%,#121110 100%)}
.slide-controls{left:145px;top:561px;width:85px;height:41px;display:flex}
.slide-controls span{flex:1;background:rgba(40,40,40,.8);display:flex;align-items:center;justify-content:center;border-right:1px solid #555}

.rule{left:144px;width:911px;height:2px;background:rgba(255,255,255,.75)}

/* steps */
.steps{left:144px;top:661px;width:911px;height:181px;display:flex}
.step{flex:1;display:flex;flex-direction:column;align-items:center;padding-top:12px;color:var(--white);font-family:"Oswald",sans-serif;font-size:18px;text-align:center;line-height:22px}
.step svg{margin-bottom:14px}
.step-label{height:46px;display:flex;align-items:center}
.step.divided{border-left:2px dotted rgba(255,255,255,.7)}
.step.current{background:var(--orange);border:2px dotted rgba(255,255,255,.6)}

/* products */
.product-panel{left:144px;top:953px;width:911px;height:836px;background:var(--panel)}
.product-grid{left:144px;top:953px;width:911px;display:grid;grid-template-columns:repeat(4,225px);column-gap:4px;row-gap:2px}
.product{height:214px;display:flex;flex-direction:column}
.product-photo{height:167px;--c1:#cfd3da;--c2:#e7e9ed;
  background:radial-gradient(ellipse 48% 42% at 50% 56%,var(--c1) 0%,var(--c2) 45%,#f4f5f7 75%,var(--tile-edge) 100%)}
.photo-yellow{--c1:#f2d21e;--c2:#f6eaa0}
.photo-van-print{--c1:#3f9a3a;--c2:#bcd8ee}
.photo-green{--c1:#2fb42f;--c2:#aee3a6}
.photo-black-yellow{--c1:#2a2a2a;--c2:#8a8460}
.photo-white-van{--c1:#c9ccd0;--c2:#eceef0}
.photo-shop{--c1:#4a4a4c;--c2:#b9b6b0}
.photo-silver-dark{--c1:#3c3e42;--c2:#b5b8bc}
.photo-silver{--c1:#6e7176;--c2:#c7c9cc}
.photo-black{--c1:#151515;--c2:#7d7f83}
.photo-sticker{--c1:#e36b2c;--c2:#8dc0d8}
.photo-clear{--c1:#9ea1a6;--c2:#d6d8db}
.photo-wheel{--c1:#56585c;--c2:#e4e5e7}
.product-label{height:47px;background:linear-gradient(180deg,var(--orange-light),var(--orange));position:relative;display:flex;align-items:center;justify-content:center;text-align:center;font-family:"Oswald",sans-serif;font-size:15px;line-height:17px;color:#3a2a18;text-transform:uppercase}
.product-label::before{content:"";position:absolute;left:8px;bottom:9px;width:11px;height:11px;border-radius:50%;background:var(--white)}

/* search */
.search-block{left:232px;top:1610px;width:729px;height:127px;background:linear-gradient(180deg,var(--orange-light),var(--orange));border-radius:6px;display:flex;align-items:center;justify-content:center;gap:10px;font-family:"Oswald",sans-serif}
.search-block label{font-size:22px;color:#7a4410}
.search-block .field{width:184px;height:30px;background:var(--white);border:1px solid #e8a24e}
.search-block .of{font-size:20px;color:#7a4410;margin:0 4px}
.search-btn{margin-left:12px;height:30px;padding:0 12px;background:var(--orange);border:1px solid #e08a1e;color:var(--white);font-size:16px;display:flex;align-items:center;gap:6px}

/* footer */
.site-footer{left:0;top:1789px;width:1200px;height:420px;background:var(--grey-dark)}
.help{left:144px;top:1820px;color:var(--white)}
.help h2{font-size:21px;font-weight:700;margin-bottom:22px}
.help ul{list-style:none}
.help li{display:flex;align-items:center;gap:12px;font-size:18px;height:22px;margin-bottom:26px;color:#eee}
.mailing{left:144px;top:2022px;color:var(--white)}
.mailing h2{font-size:21px;font-weight:700;margin-bottom:16px}
.mailing-form{display:flex;gap:8px}
.mailing-form span{height:30px;background:var(--white);border:1px solid #bbb;font-size:13px;color:#999;padding:7px 6px;font-family:"Oswald",sans-serif}
.mailing-form .subscribe{background:var(--orange);color:var(--white);border-color:var(--orange);font-size:15px;padding:5px 10px}
.compare-heading{top:1820px;font-family:"Oswald",sans-serif;font-size:21px;font-weight:400;color:var(--white)}
.compare-shot{width:170px;height:103px;border:3px solid var(--orange)}
.shot-blue-before{background:linear-gradient(160deg,#5b7ab8 0%,#1f3566 50%,#0d1426 100%)}
.shot-red-after{background:linear-gradient(160deg,#c23a3a 0%,#3a1f2a 45%,#12101a 100%)}
.shot-dark-before{background:linear-gradient(160deg,#6a6c70 0%,#2b2d30 50%,#121314 100%)}
.shot-teal-after{background:linear-gradient(160deg,#5f8a92 0%,#26393e 50%,#0f1618 100%)}
.copyright{left:144px;top:2144px;width:911px;height:65px;background:var(--grey-darker);color:#aaa;font-family:Arial,sans-serif;font-size:11px;padding:28px 0 0 30px}
</style>
</head>
<body>

<header class="site-header abs">
  <div class="brand abs"><span class="brand-dot"></span><span class="brand-name">WRAPFINDER</span></div>
  <nav class="main-nav abs">
    <a class="active" href="#">HOME</a><a href="#">ABOUT</a><a href="#">CONTACT</a><a href="#">BLOG</a><a href="#">LIST YOUR COMPANY HERE</a>
  </nav>
</header>

<div class="backdrop abs" role="img" aria-label="Blue sky over an open road stretching into the distance"></div>

<section class="tagline abs">
  <p class="tagline-lead">FIND A PROFESSIONAL VINYL INSTALLER TODAY! SEARCH AND SAVE IN SECONDS!</p>
  <p class="tagline-strong">QUICK, EASY AND FREE TO SEARCH.</p>
</section>

<div class="hero-slide abs" role="img" aria-label="White sports car parked on a city street at dusk"></div>
<div class="slide-controls abs">
  <span><svg width="12" height="18" viewBox="0 0 12 18"><path d="M9 2 2 9l7 7" stroke="#ccc" stroke-width="2" fill="none"/></svg></span>
  <span><svg width="12" height="18" viewBox="0 0 12 18"><path d="M3 2l7 7-7 7" stroke="#ccc" stroke-width="2" fill="none"/></svg></span>
</div>

<div class="rule abs" style="top:631px"></div>

<section class="steps abs">
  <div class="step">
    <svg width="92" height="92" viewBox="0 0 92 92" fill="none" stroke="#f39a2e" stroke-width="8">
      <path d="M12 54a34 34 0 1 1 68 0"/><rect x="30" y="36" width="32" height="50" rx="14" fill="#f39a2e" stroke="none"/>
    </svg>
    <div class="step-label">Select Chosen Product</div>
  </div>
  <div class="step divided">
    <svg width="92" height="92" viewBox="0 0 92 92">
      <path d="M46 6a28 28 0 0 1 28 28c0 22-28 52-28 52S18 56 18 34A28 28 0 0 1 46 6z" fill="#f39a2e"/>
      <circle cx="46" cy="32" r="12" fill="none" stroke="#0f2f86" stroke-width="5"/><path d="M54 41l9 9" stroke="#0f2f86" stroke-width="5"/>
    </svg>
    <div class="step-label">Input Postcode &amp; Distance<br>&amp; Search</div>
  </div>
  <div class="step current">
    <svg width="92" height="92" viewBox="0 0 92 92" fill="none" stroke="#0f2f86" stroke-width="5">
      <path d="M46 14v54M30 74h32M14 24h64"/><circle cx="46" cy="14" r="5" fill="#0f2f86"/>
      <path d="M14 24 4 48h20zM78 24 68 48h20z"/><path d="M4 48a10 8 0 0 0 20 0M68 48a10 8 0 0 0 20 0" fill="#0f2f86"/>
    </svg>
    <div class="step-label">Compare Companies<br>&amp; Prices</div>
  </div>
  <div class="step">
    <svg width="92" height="92" viewBox="0 0 92 92">
      <path d="M24 8c-8 0-10 8-10 18v40c0 10 2 18 10 18" stroke="#f39a2e" stroke-width="8" fill="none"/>
      <rect x="34" y="8" width="50" height="76" rx="6" fill="#f39a2e"/>
      <rect x="42" y="16" width="34" height="14" fill="#0f2f86"/>
      <g fill="#0f2f86"><rect x="42" y="38" width="8" height="8"/><rect x="55" y="38" width="8" height="8"/><rect x="68" y="38" width="8" height="8"/><rect x="42" y="52" width="8" height="8"/><rect x="55" y="52" width="8" height="8"/><rect x="68" y="52" width="8" height="8"/><rect x="42" y="66" width="8" height="8"/><rect x="55" y="66" width="8" height="8"/><rect x="68" y="66" width="8" height="8"/></g>
    </svg>
    <div class="step-label">Contact Chosen Company</div>
  </div>
</section>

<div class="rule abs" style="top:880px"></div>

<div class="product-panel abs"></div>
<section class="product-grid abs">
  <div class="product"><div class="product-photo photo-yellow" role="img" aria-label="Yellow convertible with a colour change wrap"></div><div class="product-label">Colour Change<br>Wrap</div></div>
  <div class="product"><div class="product-photo photo-van-print" role="img" aria-label="Van with a printed green and sky vehicle wrap"></div><div class="product-label">Printed Vehicle<br>Wrap</div></div>
  <div class="product"><div class="product-photo photo-green" role="img" aria-label="Two green hatchbacks with tinted windows"></div><div class="product-label">Window Tint</div></div>
  <div class="product"><div class="product-photo photo-black-yellow" role="img" aria-label="Black muscle car front with tinted headlights"></div><div class="product-label">Headlight Tint</div></div>
  <div class="product"><div class="product-photo photo-white-van" role="img" aria-label="White van with signage lettering"></div><div class="product-label">Vehicle Signage</div></div>
  <div class="product"><div class="product-photo photo-shop" role="img" aria-label="Shop front with window signage"></div><div class="product-label">Shop Signage</div></div>
  <div class="product"><div class="product-photo photo-silver-dark" role="img" aria-label="Silver car with a black roof wrap"></div><div class="product-label">Roof Vinyl<br>Wrap</div></div>
  <div class="product"><div class="product-photo photo-silver" role="img" aria-label="Silver car with a dark bonnet wrap"></div><div class="product-label">Bonnet Vinyl<br>Wrap</div></div>
  <div class="product"><div class="product-photo photo-black" role="img" aria-label="Black SUV with carbon fibre vinyl"></div><div class="product-label">Carbon Fibre<br>Vinyl</div></div>
  <div class="product"><div class="product-photo photo-sticker" role="img" aria-label="White sports car with a colourful stickerbomb bonnet"></div><div class="product-label">Stickerbomb Vinyl</div></div>
  <div class="product"><div class="product-photo photo-clear" role="img" aria-label="Silver car with clear protective film"></div><div class="product-label">Clear Protective<br>Vinyl</div></div>
  <div class="product"><div class="product-photo photo-wheel" role="img" aria-label="Refurbished alloy wheel on a white car"></div><div class="product-label">Wheel Refurb</div></div>
</section>

<form class="search-block abs">
  <label>SEARCH WITHIN</label><span class="field"></span><span class="of">OF</span><span class="field"></span>
  <span class="search-btn"><svg width="12" height="12" viewBox="0 0 12 12"><circle cx="5" cy="5" r="3.5" stroke="#fff" stroke-width="1.6" fill="none"/><path d="M7.5 7.5 11 11" stroke="#fff" stroke-width="1.6"/></svg>SEARCH</span>
</form>

<footer class="site-footer abs"></footer>
<section class="help abs">
  <h2>How can Wrapfinder help you?</h2>
  <ul>
    <li><svg width="18" height="16" viewBox="0 0 18 16"><path d="M2 8l5 5L16 2" stroke="var(--tick)" stroke-width="3.5" fill="none"/></svg>Compare Products, Locations and Prices.</li>
    <li><svg width="18" height="16" viewBox="0 0 18 16"><path d="M2 8l5 5L16 2" stroke="var(--tick)" stroke-width="3.5" fill="none"/></svg>Installers throughout the Country.</li>
    <li><svg width="18" height="16" viewBox="0 0 18 16"><path d="M2 8l5 5L16 2" stroke="var(--tick)" stroke-width="3.5" fill="none"/></svg>Available throughout the Country.</li>
  </ul>
</section>
<section class="mailing abs">
  <h2>Join our Mailing List</h2>
  <div class="mailing-form">
    <span style="width:141px">Name</span><span style="width:183px">Email address</span><span class="subscribe">SUBSCRIBE</span>
  </div>
</section>

<h3 class="compare-heading abs" style="left:651px">Before</h3>
<h3 class="compare-heading abs" style="left:848px">After</h3>
<div class="compare-shot shot-blue-before abs" style="left:651px;top:1862px" role="img" aria-label="Blue coupe before wrapping"></div>
<div class="compare-shot shot-red-after abs" style="left:848px;top:1862px" role="img" aria-label="Coupe after a red stripe wrap"></div>
<div class="compare-shot shot-dark-before abs" style="left:651px;top:1989px" role="img" aria-label="Dark saloon before wrapping"></div>
<div class="compare-shot shot-teal-after abs" style="left:848px;top:1989px" role="img" aria-label="Saloon after a colour change wrap"></div>

<div class="copyright abs">Copyright © 2013 Wrapfinder. All rights reserved.</div>

</body>
</html>
```